Business Card Design

We need a business card design that can also be aplied for postcards. We are a small indie record company that also do consulting, and development of independat artitst . I already have the name and the basic idea of what i am looking for but i am open to any suggestion.
Info for the card
Name of the company : Velmora Records
NAME : Tobias Lindqvist
PHONE : 314-5820641
EMAIL : hello@velmorarecords.example
WEB: www.velmorarecords.example
Target Market(s)
Male - Female independent musicians ages 18 to 45
Industry/Entity Type
Record Company
Contact Information for Business Card
Independant records company that also works in consulting for music business models for independent artists
Look and feel

```html
<!DOCTYPE html>
<html lang="en">
<head>
<meta charset="utf-8">
<title>Velmora Records – Business Card</title>
<link href="https://fonts.googleapis.com/css2?family=Cookie&family=Arimo:wght@700&display=swap" rel="stylesheet">
<style>
  :root {
    --blue-deep: #0b5fb3;
    --blue-mid: #2a8fdc;
    --blue-light: #9fd0f2;
    --blue-pale: #eef7fd;
    --band: #0c5886;
    --band-stripe: #4a92c4;
    --white: #ffffff;
  }
  html, body {
    margin: 0;
    padding: 0;
    width: 1200px;
    height: 704px;
    overflow: hidden;
    background: var(--white);
  }
  .card {
    position: relative;
    width: 1200px;
    height: 704px;
    overflow: hidden;
    font-family: "Arimo", Arial, sans-serif;
    color: var(--white);
  }
  .card__backdrop {
    position: absolute;
    inset: 0;
    background:
      radial-gradient(ellipse 520px 300px at 880px 360px, var(--blue-pale) 0%, rgba(238,247,253,0.85) 35%, rgba(238,247,253,0) 100%),
      radial-gradient(ellipse 700px 420px at 1150px 520px, var(--white) 0%, rgba(255,255,255,0) 70%),
      linear-gradient(160deg, var(--blue-deep) 0%, var(--blue-mid) 38%, var(--blue-light) 70%, var(--blue-pale) 100%);
  }
  .card__title {
    position: absolute;
    left: 0;
    right: 0;
    top: 148px;
    margin: 0;
    text-align: center;
    font-family: "Cookie", cursive;
    font-weight: 400;
    font-size: 118px;
    line-height: 1;
    color: var(--white);
  }
  .card__footer {
    position: absolute;
    left: 0;
    top: 513px;
    width: 1200px;
    height: 191px;
  }
  .card__footer svg {
    position: absolute;
    inset: 0;
  }
  .contact-name {
    position: absolute;
    left: 77px;
    top: 50px;
    margin: 0;
    font-size: 49px;
    font-weight: 700;
    letter-spacing: -0.5px;
    transform: scaleX(0.92);
    transform-origin: left center;
  }
  .contact-email,
  .contact-web {
    position: absolute;
    right: 46px;
    margin: 0;
    font-size: 29px;
    font-weight: 700;
    text-align: right;
  }
  .contact-email { top: 28px; }
  .contact-web { top: 94px; }
  .contact-phone {
    position: absolute;
    left: 844px;
    width: 200px;
    top: 132px;
    margin: 0;
    text-align: center;
    font-size: 23px;
    font-weight: 700;
  }
</style>
</head>
<body>
  <div class="card">
    <div class="card__backdrop" role="img" aria-label="Abstract background of flowing blue light streaks fading to pale blue"></div>

    <h1 class="card__title">Velmora Records</h1>

    <footer class="card__footer">
      <svg width="1200" height="191" viewBox="0 0 1200 191" aria-hidden="true">
        <rect class="band" x="0" y="0" width="1200" height="163" fill="var(--band)"/>
        <polygon class="band-stripe" points="0,163 1200,163 1200,183 0,183" fill="var(--band-stripe)"/>
        <polygon class="band-cut" points="528,163 1200,163 1200,183 505,183" fill="var(--white)"/>
        <rect class="band-base" x="0" y="183" width="1200" height="8" fill="var(--band)"/>
        <rect class="band-rule" x="688" y="78" width="512" height="3" fill="var(--white)"/>
      </svg>
      <p class="contact-name">Tobias Lindqvist</p>
      <p class="contact-email">hello@velmorarecords.example</p>
      <p class="contact-web">www.velmorarecords.example</p>
      <p class="contact-phone">314-5820641</p>
    </footer>
  </div>
</body>
</html>
```